Mosquito Repellent Wet Wipes pacakage design

We are a mosquito repellent manufacturer under the brand name "Zap Clear". We have a product currently and are looking to make it more attractive.

Our product is a mosquito repellent wipe that can be applied on skin and clothing for protection against mosquitoes. It is going to be available in sachets. Customer age groups include ages 10-30 as well as Moms who are key decision makers.

We are looking for a friendly package in terms of color and appeal and a redesign of Zap Clear logo. I am attaching our current product pictures and brochure. Hope this gets you started. We are attaching information on the spray bottle.

Visit www.velmorahealth.example for more details.

Package Dimension Folded : 80x60 mm
Package Dimension unfolded: 80 x 120 mm

Thank you
Ravi

Target Market(s)

General population with more focus on age groups 10-30 as well as Moms

Industry/Entity Type

Cosmetics

Requirements
Must have
• Statutory information should be provided on the product including Manufacturing address, ingredient name & bar code. I guess we can do this once the package is finalized

```html
<!DOCTYPE html>
<html lang="en">
<head>
<meta charset="utf-8">
<title>Zap Clear – Mosquito Repellent Wipes Sachet</title>
<link href="https://fonts.googleapis.com/css2?family=Oswald:wght@500;600&family=Open+Sans:ital,wght@1,600&display=swap" rel="stylesheet">
<style>
  :root {
    --page: #ffffff;
    --leaf-bright: #9bd82c;
    --leaf-light: #d4f266;
    --leaf-deep: #6fb51c;
    --ink-dark: #1d2a08;
    --panel-dark: #1b2409;
    --panel-text: #f3f4df;
    --seal-line: rgba(255, 255, 255, 0.55);
    --tagline: #fbfdf0;
  }
  html, body {
    margin: 0;
    padding: 0;
    width: 1200px;
    height: 866px;
    overflow: hidden;
    background: var(--page);
  }
  .canvas {
    position: relative;
    width: 1200px;
    height: 866px;
  }
  .sachet {
    position: absolute;
    left: 398px;
    top: 156px;
    width: 430px;
    height: 586px;
    overflow: hidden;
    background:
      radial-gradient(ellipse 60% 45% at 55% 42%, var(--leaf-light) 0%, rgba(212,242,102,0) 70%),
      radial-gradient(ellipse 40% 30% at 25% 20%, rgba(230,250,150,0.7) 0%, rgba(230,250,150,0) 70%),
      linear-gradient(160deg, var(--leaf-bright) 0%, #a9e03a 45%, var(--leaf-deep) 100%);
  }
  .seal {
    position: absolute;
    left: 0;
    right: 0;
    height: 8px;
    border-top: 1px solid var(--seal-line);
    border-bottom: 1px solid var(--seal-line);
  }
  .seal--top { top: 18px; }
  .seal--bottom { top: 556px; }
  .pack-count {
    position: absolute;
    right: 28px;
    top: 38px;
    margin: 0;
    font-family: "Oswald", sans-serif;
    font-weight: 600;
    font-size: 36px;
    line-height: 1;
    color: var(--panel-text);
    font-variant: small-caps;
    letter-spacing: 0.5px;
  }
  .mascot-art {
    position: absolute;
    left: 56px;
    top: 214px;
    width: 130px;
    height: 160px;
    border-radius: 50%;
    background: radial-gradient(ellipse at 50% 45%, #7c8a3a 0%, rgba(124,138,58,0.35) 55%, rgba(124,138,58,0) 75%);
  }
  .brand {
    position: absolute;
    left: 170px;
    top: 150px;
    display: flex;
    align-items: center;
    gap: 10px;
  }
  .brand__dot {
    width: 22px;
    height: 22px;
    border-radius: 50%;
    background: var(--ink-dark);
  }
  .brand__name {
    margin: 0;
    font-family: "Oswald", sans-serif;
    font-weight: 600;
    font-size: 64px;
    line-height: 0.95;
    color: var(--ink-dark);
  }
  .product-type {
    position: absolute;
    left: 0;
    right: 0;
    top: 404px;
    margin: 0;
    text-align: center;
    font-family: "Oswald", sans-serif;
    font-weight: 500;
    font-size: 30px;
    line-height: 1.2;
    color: var(--ink-dark);
    letter-spacing: 0.2px;
    white-space: nowrap;
  }
  .claim-panel {
    position: absolute;
    left: 32px;
    top: 449px;
    width: 373px;
    height: 71px;
    box-sizing: border-box;
    padding: 4px 6px;
    border-radius: 8px;
    background: var(--panel-dark);
    color: var(--panel-text);
    font-family: "Oswald", sans-serif;
    font-weight: 600;
    text-align: center;
    display: flex;
    flex-direction: column;
    justify-content: center;
    gap: 2px;
    white-space: nowrap;
    overflow: hidden;
  }
  .claim-panel__lead {
    font-size: 25px;
    line-height: 1;
    font-variant: small-caps;
    letter-spacing: 0.8px;
  }
  .claim-panel__diseases {
    font-size: 25px;
    line-height: 1.1;
    letter-spacing: 0.3px;
  }
  .tagline {
    position: absolute;
    left: 0;
    right: 0;
    top: 522px;
    margin: 0;
    text-align: center;
    font-family: "Open Sans", sans-serif;
    font-style: italic;
    font-weight: 600;
    font-size: 22px;
    color: var(--tagline);
    white-space: nowrap;
  }
</style>
</head>
<body>
<main class="canvas">
  <section class="sachet" aria-label="Zap Clear mosquito repellent wipe sachet, front">
    <div class="seal seal--top"></div>
    <p class="pack-count">1 Wipe</p>
    <div class="mascot-art" role="img" aria-label="Cartoon mosquito mascot illustration"></div>
    <div class="brand">
      <span class="brand__dot"></span>
      <h1 class="brand__name">Zap<br>Clear</h1>
    </div>
    <h2 class="product-type">MOSQUITO REPELLENT WIPES</h2>
    <div class="claim-panel">
      <span class="claim-panel__lead">Repels Mosquitoes that may carry</span>
      <span class="claim-panel__diseases">MALARIA, CHIKUNGUNYA &amp; DENGUE</span>
    </div>
    <p class="tagline">light and fresh with olive extracts</p>
    <div class="seal seal--bottom"></div>
  </section>
</main>
</body>
</html>
```